Book Cover Design GML

Want a new book cover but want to use the same photo and change the sub name. This is for a brand called "Golden Maple Living". The book is called "Just Steps, Just Results"

This is for a 8.5 * 11 book size

We really want to brand the Golden Maple Living

I've attached a sample of an old book cover, the photo I want used and the golden maple living logo

Requirements
Must have
• Must have the logo,

must have the book title. "Just Steps, Just Results"

Must have "Featuring" The Golden Maple Living Fit Roll Card Game"

On the back put the logo and Golden Maple Living Nutrition

must have the authors name "Dana Holcomb" on the page

"The Prime Shape Roadmap"
Nice to have
• Golden Maple Living Presents:

the book title

```html
<!DOCTYPE html>
<html lang="en">
<head>
<meta charset="utf-8">
<title>Just Steps, Just Results — Dana Holcomb</title>
<link rel="stylesheet" href="https://fonts.googleapis.com/css2?family=Open+Sans:wdth,wght@75..100,300..800&family=Oswald:wght@700&display=swap">
<style>
  :root {
    --cover-bg: #130b08;
    --gold: #fcc870;
    --gold-deep: #4a2a18;
    --ink-light: #ffffff;
    --photo-warm: #5a3a2a;
    --photo-green: #3f8a6c;
  }
  html, body {
    margin: 0;
    padding: 0;
    width: 930px;
    height: 1200px;
    overflow: hidden;
    background: var(--cover-bg);
  }
  .book-cover {
    display: block;
    width: 930px;
    height: 1200px;
    font-family: "Open Sans", sans-serif;
    font-stretch: 75%;
  }
  .series-line {
    fill: var(--ink-light);
    font-weight: 300;
    font-size: 32px;
  }
  .title-main {
    font-family: "Oswald", "Open Sans", sans-serif;
    font-weight: 700;
  }
  .title-gold { fill: url(#titleGold); }
  .title-white { fill: var(--ink-light); }
  .subtitle {
    fill: var(--ink-light);
    font-size: 46px;
    letter-spacing: 6px;
  }
  .subtitle-light { font-weight: 300; }
  .subtitle-bold { font-weight: 700; }
  .gold-bar { fill: var(--gold); }
  .featuring-label {
    fill: var(--ink-light);
    font-weight: 700;
    font-size: 24px;
    letter-spacing: 4px;
  }
  .featuring-title {
    fill: var(--ink-light);
    font-weight: 300;
    letter-spacing: 2px;
  }
  .author {
    fill: var(--ink-light);
    font-size: 37px;
    letter-spacing: 4px;
  }
  .author-first { font-weight: 300; }
  .author-last { font-weight: 700; }
  .brand-mark { fill: var(--gold); }
  .brand-name {
    fill: var(--gold);
    font-weight: 700;
    font-size: 22px;
    letter-spacing: 3px;
  }
</style>
</head>
<body>
<svg class="book-cover" viewBox="0 0 930 1200" xmlns="http://www.w3.org/2000/svg">
  <defs>
    <linearGradient id="titleGold" x1="0" y1="113" x2="0" y2="283" gradientUnits="userSpaceOnUse">
      <stop offset="0" stop-color="var(--gold-deep)"/>
      <stop offset="0.55" stop-color="var(--gold)"/>
      <stop offset="1" stop-color="var(--gold)"/>
    </linearGradient>
    <linearGradient id="photoTone" x1="0" y1="0" x2="1" y2="1">
      <stop offset="0" stop-color="var(--photo-green)"/>
      <stop offset="0.55" stop-color="var(--photo-warm)"/>
      <stop offset="1" stop-color="#1e1410"/>
    </linearGradient>
  </defs>

  <rect width="930" height="1200" fill="var(--cover-bg)"/>

  <g role="img" aria-label="Photo of the author in a black sports top and leggings, resting her arm on a green exercise ball">
    <circle cx="494" cy="769" r="159" fill="url(#photoTone)"/>
    <rect x="680" y="470" width="225" height="730" rx="60" fill="url(#photoTone)"/>
  </g>

  <text class="series-line" x="104" y="76" textLength="706" lengthAdjust="spacingAndGlyphs">THE GOLDEN MAPLE LIVING FIT ROLL CARD GAME</text>

  <text class="title-main title-gold" x="104" y="283" font-size="212" textLength="720" lengthAdjust="spacingAndGlyphs">JUST STEPS<tspan dy="-14">,</tspan></text>
  <text class="title-main title-white" x="104" y="458" font-size="206" textLength="734" lengthAdjust="spacingAndGlyphs">JUST RESULTS</text>

  <g class="subtitle">
    <text class="subtitle-light" x="104" y="588">THE</text>
    <text class="subtitle-bold" x="104" y="632">PRIME</text>
    <text class="subtitle-bold" x="104" y="676">SHAPE</text>
    <text class="subtitle-light" x="104" y="720">ROADMAP</text>
  </g>

  <rect class="gold-bar" x="104" y="843" width="260" height="19"/>
  <rect class="gold-bar" x="104" y="984" width="390" height="20"/>

  <text class="featuring-label" x="115" y="898">FEATURING:</text>
  <text class="featuring-title" x="115" y="932" font-size="17">“THE GOLDEN MAPLE</text>
  <text class="featuring-title" x="115" y="960" font-size="28">LIVING FIT ROLL</text>
  <text class="featuring-title" x="115" y="979" font-size="15">CARD GAME”</text>

  <text class="author" x="385" y="1065" text-anchor="middle"><tspan class="author-first">DANA </tspan><tspan class="author-last">HOLCOMB</tspan></text>

  <g class="brand">
    <circle class="brand-mark" cx="116" cy="1138" r="10"/>
    <text class="brand-name" x="136" y="1146">GOLDEN MAPLE LIVING</text>
  </g>
</svg>
</body>
</html>
```